Recruiting ad for Caregivers and Nurses

We need a few amazing, fun, catchy, creative recruiting ads for Caregivers and Nurses to care for homecare patients on the island of Oahu, in Hawaii. We are an in home care company called Brantley Homecare. Our care services are provided 24/7, so we need staff that can work days, nights, weekdays, weekends. We need catchy fun ads to entice caregivers and nurses to call our office to inquire about jobs available. Our patients age range is from babies to seniors. We need caregivers and nurses for basic patient care (bathing, dressing, ambulating, preparing meals, medication reminders, light housekeeping) and complex patients (oxygen, tube feeding, injections, vents, wound care). Here are some bullets to consider including:
*Full-time and Part-time Positions Available (days, nights, weekdays, weekends)
*Sign-On Bonus Programs Offered up to $500
*Refer a Friend Bonus Program
*Holiday Pay
*2 Health Plans to Choose from
*Island-Wide Locations
*All PPE Provided (masks, gloves, etc)
*401K Program
*Tuition Benefits

```html
<!DOCTYPE html>
<html lang="en">
<head>
<meta charset="utf-8">
<title>Brantley Homecare – Caregivers and Nurses</title>
<link rel="stylesheet" href="https://fonts.googleapis.com/css2?family=Tenor+Sans&family=Alegreya+Sans:wght@400;500;700&display=swap">
<style>
  :root {
    --teal: #00756a;
    --salmon: #f59e82;
    --salmon-deep: #f4826a;
    --shadow-grey: #dcdcdc;
    --ink: #231f20;
    --white: #ffffff;
    --paper: #fbfbfb;
  }
  * { margin: 0; padding: 0; box-sizing: border-box; }
  html, body { width: 798px; height: 1200px; overflow: hidden; background: var(--paper); }
  .flyer { position: relative; width: 798px; height: 1200px; overflow: hidden; background: var(--paper); }
  .shapes { position: absolute; inset: 0; }

  .brand { position: absolute; left: 60px; top: 40px; width: 230px; text-align: center; }
  .brand-mark { width: 64px; height: 52px; margin: 0 auto 30px; background: var(--salmon); border-radius: 8px; }
  .brand-name {
    font-family: "Tenor Sans", sans-serif; color: var(--teal);
    font-size: 34px; line-height: 1.1; letter-spacing: 0.5px;
  }

  .hours-badge {
    position: absolute; left: 63px; top: 246px; width: 208px; height: 208px; border-radius: 50%;
    background: var(--teal); color: var(--white); text-align: center;
    font-family: "Tenor Sans", sans-serif; display: flex; flex-direction: column; justify-content: center;
  }
  .hours-badge .lead { font-size: 26px; line-height: 1.15; }
  .hours-badge .lead:first-child { font-size: 22px; }
  .hours-badge .hours { font-family: "Alegreya Sans", sans-serif; font-weight: 700; font-size: 46px; line-height: 1.1; margin-top: 2px; }

  .photo {
    position: absolute; left: 351px; top: 47px; width: 400px; height: 400px; border-radius: 50%;
    background: radial-gradient(circle at 55% 45%, #e8d6cc 0%, #d9e4ec 40%, #eef0f0 75%, #f4f4f4 100%);
  }

  .headline {
    position: absolute; left: 82px; top: 485px;
    font-family: "Tenor Sans", sans-serif; color: var(--teal); font-size: 72px; line-height: 80px;
  }
  .headline span { display: block; }
  .subline {
    position: absolute; left: 86px; top: 655px; width: 660px;
    font-family: "Tenor Sans", sans-serif; color: var(--ink); font-size: 40px; line-height: 52px;
  }

  .services { position: absolute; left: 60px; top: 818px; width: 690px; font-family: "Alegreya Sans", sans-serif; }
  .services-title { color: var(--teal); font-weight: 700; font-size: 32px; line-height: 31px; }
  .services-title span { display: block; padding-left: 26px; }
  .services-title span + span { padding-left: 0; }
  .perk-lists { display: flex; margin-top: 14px; }
  .perk-list { list-style: none; color: var(--white); font-weight: 500; font-size: 17px; line-height: 20.5px; }
  .perk-list:first-child { width: 387px; }
  .perk-list li { position: relative; padding-left: 24px; }
  .perk-list li svg { position: absolute; left: 0; top: 4px; width: 13px; height: 13px; }
  .perk-note { display: block; font-weight: 400; }

  .cta-bar {
    position: absolute; left: 60px; top: 1030px; width: 679px; height: 39px; background: var(--teal);
    color: var(--white); font-family: "Alegreya Sans", sans-serif; font-weight: 500; font-size: 21px;
    display: flex; align-items: center; justify-content: center;
  }
  .contact {
    position: absolute; left: 58px; top: 1092px; width: 682px; display: flex; justify-content: space-between;
    font-family: "Alegreya Sans", sans-serif; font-weight: 700; font-size: 38px; color: var(--ink);
  }
</style>
</head>
<body>
<main class="flyer">
  <svg class="shapes" width="798" height="1200" viewBox="0 0 798 1200" aria-hidden="true">
    <defs>
      <clipPath id="footer-clip">
        <path d="M0,812 C250,790 520,798 798,762 L798,1200 L0,1200 Z"/>
      </clipPath>
    </defs>
    <path class="ribbon" fill="var(--salmon)" d="M0,500 C50,400 120,305 240,292 L440,287 L440,381 L250,386 C150,392 70,440 0,470 Z"/>
    <circle class="ring-shadow" cx="545" cy="276" r="230" fill="var(--shadow-grey)"/>
    <path class="ring-tail" fill="var(--salmon)" d="M700,150 C740,140 775,160 798,175 L798,200 C770,210 750,250 740,300 Z"/>
    <circle class="ring" cx="560" cy="268" r="226" fill="var(--salmon)"/>
    <circle class="ring-inner" cx="551" cy="247" r="209" fill="var(--white)"/>
    <path class="wave" fill="var(--teal)" d="M0,805 C220,760 520,778 798,718 L798,746 C520,796 240,782 0,812 Z"/>
    <path class="footer" fill="var(--salmon)" d="M0,812 C250,790 520,798 798,762 L798,1200 L0,1200 Z"/>
    <rect class="footer-panel" x="602" y="760" width="196" height="440" fill="var(--salmon-deep)" clip-path="url(#footer-clip)"/>
  </svg>

  <div class="brand">
    <div class="brand-mark"></div>
    <div class="brand-name">Brantley Homecare</div>
  </div>

  <div class="photo" role="img" aria-label="Photo of a smiling nurse in blue scrubs with her hands on the shoulders of a smiling senior woman"></div>

  <div class="hours-badge">
    <span class="lead">Our care</span>
    <span class="lead">services are</span>
    <span class="lead">provided</span>
    <span class="hours">24/7</span>
  </div>

  <h1 class="headline"><span>Caregivers</span><span>and Nurses to care</span></h1>
  <p class="subline">for homecare patients on the island of Oahu, in Hawaii.</p>

  <section class="services">
    <h2 class="services-title"><span>Our</span><span>Care Services</span></h2>
    <div class="perk-lists">
      <ul class="perk-list">
        <li><svg viewBox="0 0 13 13"><rect x="0.75" y="1.75" width="10.5" height="10.5" fill="none" stroke="var(--teal)" stroke-width="1.5"/><path d="M3,6.5 L6,9.5 L12.5,1" fill="none" stroke="var(--teal)" stroke-width="2"/></svg>Full-time and Part-time Positions Available<span class="perk-note">(days, nights, weekdays, weekends)</span></li>
        <li><svg viewBox="0 0 13 13"><rect x="0.75" y="1.75" width="10.5" height="10.5" fill="none" stroke="var(--teal)" stroke-width="1.5"/><path d="M3,6.5 L6,9.5 L12.5,1" fill="none" stroke="var(--teal)" stroke-width="2"/></svg>Sign-On Bonus Programs Offered up to $500</li>
        <li><svg viewBox="0 0 13 13"><rect x="0.75" y="1.75" width="10.5" height="10.5" fill="none" stroke="var(--teal)" stroke-width="1.5"/><path d="M3,6.5 L6,9.5 L12.5,1" fill="none" stroke="var(--teal)" stroke-width="2"/></svg>Refer a Friend Bonus Program</li>
        <li><svg viewBox="0 0 13 13"><rect x="0.75" y="1.75" width="10.5" height="10.5" fill="none" stroke="var(--teal)" stroke-width="1.5"/><path d="M3,6.5 L6,9.5 L12.5,1" fill="none" stroke="var(--teal)" stroke-width="2"/></svg>Holiday Pay</li>
      </ul>
      <ul class="perk-list">
        <li><svg viewBox="0 0 13 13"><rect x="0.75" y="1.75" width="10.5" height="10.5" fill="none" stroke="var(--teal)" stroke-width="1.5"/><path d="M3,6.5 L6,9.5 L12.5,1" fill="none" stroke="var(--teal)" stroke-width="2"/></svg>2 Health Plans to Choose from</li>
        <li><svg viewBox="0 0 13 13"><rect x="0.75" y="1.75" width="10.5" height="10.5" fill="none" stroke="var(--teal)" stroke-width="1.5"/><path d="M3,6.5 L6,9.5 L12.5,1" fill="none" stroke="var(--teal)" stroke-width="2"/></svg>Island-Wide Locations</li>
        <li><svg viewBox="0 0 13 13"><rect x="0.75" y="1.75" width="10.5" height="10.5" fill="none" stroke="var(--teal)" stroke-width="1.5"/><path d="M3,6.5 L6,9.5 L12.5,1" fill="none" stroke="var(--teal)" stroke-width="2"/></svg>All PPE Provided (masks, gloves, etc)</li>
        <li><svg viewBox="0 0 13 13"><rect x="0.75" y="1.75" width="10.5" height="10.5" fill="none" stroke="var(--teal)" stroke-width="1.5"/><path d="M3,6.5 L6,9.5 L12.5,1" fill="none" stroke="var(--teal)" stroke-width="2"/></svg>401K Program</li>
        <li><svg viewBox="0 0 13 13"><rect x="0.75" y="1.75" width="10.5" height="10.5" fill="none" stroke="var(--teal)" stroke-width="1.5"/><path d="M3,6.5 L6,9.5 L12.5,1" fill="none" stroke="var(--teal)" stroke-width="2"/></svg>Tuition Benefits</li>
      </ul>
    </div>
  </section>

  <div class="cta-bar">Caregivers and Nurses to call our office to inquire about jobs available</div>

  <div class="contact">
    <span class="phone">Call: 808-555-0173</span>
    <span class="web">brantleycare.com</span>
  </div>
</main>
</body>
</html>
```